Ferris Contracting LLC Business Card Design

I am looking for a creative and unique business card design. We are a commercial construction general contractor. With the name "FERRIS" Contracting, I am hoping to see some neat designs that correlate with the name.

```html
<!DOCTYPE html>
<html lang="en">
<head>
<meta charset="utf-8">
<title>Ferris Contracting LLC – Business Card</title>
<link rel="stylesheet" href="https://fonts.googleapis.com/css2?family=Roboto:wght@400;500;700;900&display=swap">
<style>
  :root {
    --page-bg: #d9d6d1;
    --card-dark: #1d1d1f;
    --card-glow: #2c2c2f;
    --brand-blue: #1f8ed8;
    --brand-blue-deep: #0f6cb3;
    --steel: #c4c6c9;
    --steel-dark: #8d9094;
    --text-light: #eeeeee;
    --text-muted: #c9c9c9;
  }
  * { margin: 0; padding: 0; box-sizing: border-box; }
  html, body {
    width: 1200px; height: 900px; overflow: hidden;
    background: var(--page-bg);
    font-family: "Roboto", Arial, sans-serif;
  }
  .sheet {
    position: relative; width: 1200px; height: 900px;
    display: flex; flex-direction: column; align-items: center;
    justify-content: center; gap: 40px;
  }
  .card {
    position: relative; width: 700px; height: 400px; overflow: hidden;
    background: radial-gradient(circle at 50% 50%, var(--card-glow) 0%, var(--card-dark) 65%);
    box-shadow: 0 10px 28px rgba(0,0,0,.35);
  }
  .brand {
    position: absolute; display: flex; align-items: center; gap: 14px;
    color: var(--brand-blue); font-weight: 900; text-transform: uppercase;
    line-height: 1; letter-spacing: 2px;
  }
  .brand-dot {
    width: 46px; height: 46px; border-radius: 50%;
    background: var(--brand-blue); flex: none;
  }
  .brand-name { font-size: 34px; }
  .brand-name span { display: block; font-size: 34px; }
  .card--front .brand { left: 50%; top: 50%; transform: translate(-50%, -50%); }
  .card--back .brand { right: 46px; top: 150px; }
  .card--back .brand-dot { width: 38px; height: 38px; }
  .card--back .brand-name, .card--back .brand-name span { font-size: 28px; }

  .sweep { position: absolute; inset: 0; }

  .contact {
    position: absolute; left: 42px; top: 92px; color: var(--text-light);
  }
  .contact-name {
    color: var(--brand-blue); font-weight: 700; font-size: 22px;
    text-transform: uppercase; letter-spacing: .5px;
  }
  .contact-role { font-size: 15px; color: var(--text-muted); margin-bottom: 20px; }
  .contact-list { list-style: none; }
  .contact-list li {
    display: flex; align-items: center; gap: 10px;
    font-size: 17px; margin-bottom: 6px;
  }
  .contact-list svg { width: 16px; height: 16px; flex: none; }
  .contact-rule {
    width: 190px; height: 1px; background: var(--brand-blue);
    margin: 12px 0 12px 26px;
  }
  .contact-address { font-size: 17px; line-height: 1.25; padding-left: 26px; }
</style>
</head>
<body>
<main class="sheet">

  <section class="card card--front" aria-label="Card front">
    <div class="brand">
      <div class="brand-dot"></div>
      <div class="brand-name">Ferris<span>Contracting</span></div>
    </div>
  </section>

  <section class="card card--back" aria-label="Card back">
    <svg class="sweep" viewBox="0 0 700 400" aria-hidden="true">
      <circle cx="30" cy="250" r="395" fill="var(--steel)"/>
      <circle cx="26" cy="252" r="372" fill="var(--card-dark)"/>
      <circle cx="20" cy="256" r="352" fill="var(--brand-blue)"/>
      <circle cx="2" cy="262" r="338" fill="#232326"/>
    </svg>

    <div class="contact">
      <div class="contact-name">Daniel Reyes</div>
      <div class="contact-role">Owner</div>
      <ul class="contact-list">
        <li>
          <svg viewBox="0 0 16 16"><path d="M4 1.5l2.2 3-1.3 1.6c.8 1.8 2.2 3.2 4 4l1.6-1.3 3 2.2-1.2 2.5C6.6 13.3 2.7 9.4 1.5 3.8z" fill="var(--brand-blue)"/></svg>
          300-555-0142
        </li>
        <li>
          <svg viewBox="0 0 16 16"><rect x="1" y="3" width="14" height="10" fill="var(--brand-blue)"/><path d="M1 3l7 6 7-6" stroke="#1d1d1f" stroke-width="1.4" fill="none"/></svg>
          info@ferris.com
        </li>
        <li>
          <svg viewBox="0 0 16 16" fill="none" stroke="var(--brand-blue)" stroke-width="1.3"><circle cx="8" cy="8" r="6.5"/><ellipse cx="8" cy="8" rx="3" ry="6.5"/><path d="M1.5 8h13M3 4.5h10M3 11.5h10"/></svg>
          www.ferris.com
        </li>
      </ul>
      <div class="contact-rule"></div>
      <p class="contact-address">00 dummy city<br>dummy place 0000</p>
    </div>

    <div class="brand">
      <div class="brand-dot"></div>
      <div class="brand-name">Ferris<span>Contracting</span></div>
    </div>
  </section>

</main>
</body>
</html>
```